Plakat-Design für Garten- und Landschaftsbau
Zielgruppe
Unsere Firma beschäftigt sich mit dem Garten- und Landschaftsbau, das heißt wie gestalten Gärten neu, führen Baggerarbeiten und Erdarbeiten durch.
Und sind in dem Forst und Rodungsarbeiten aktiv
Aufgabenstellung
Dies soll ein Banner sein das an Bauzäune angebracht wird Format bzw. Verhältnis sollte bxh 2:1 sein
Der Banner soll mit einen oder meheren Bildern versehen werden im Hintergrund oder im Vordergrund.

```html
<!DOCTYPE html>
<html lang="de">
<head>
<meta charset="utf-8">
<title>Grünwerk Kessler – Bauzaunbanner</title>
<link href="https://fonts.googleapis.com/css2?family=Baloo+2:wght@700;800&family=Roboto:ital,wght@1,700&display=swap" rel="stylesheet">
<style>
  :root {
    --page: #eaf6fe;
    --sky-top: #aadcfb;
    --sky-low: #dcedf9;
    --lawn: #5fae2e;
    --panel-top: #43991f;
    --panel-bottom: #1f640d;
    --logo-green: #0b7a3a;
    --slate: #4a4f57;
    --white: #ffffff;
    --yellow: #f7d800;
    --yellow-deep: #f2c200;
    --ink-green: #1f5a0a;
  }
  html, body { margin: 0; padding: 0; }
  body {
    width: 1200px; height: 1200px; overflow: hidden;
    background: var(--page);
    font-family: "Baloo 2", sans-serif;
  }
  .banner {
    position: absolute; left: 85px; top: 342px;
    width: 1030px; height: 515px; overflow: hidden;
  }
  .photo {
    position: absolute; inset: 0;
    background: linear-gradient(180deg, var(--sky-top) 0%, var(--sky-low) 45%, #b9c3cc 62%, #8f9aa3 72%, var(--lawn) 86%, #4d9a25 100%);
  }
  .brand {
    position: absolute; left: 55px; top: 62px; width: 400px;
  }
  .brand-name {
    margin: 0; font-weight: 800; font-size: 46px; line-height: 1;
    color: var(--logo-green); letter-spacing: 0.5px;
  }
  .brand-rule { height: 3px; background: var(--logo-green); margin: 8px 0 6px; }
  .brand-tagline {
    margin: 0; font-family: "Roboto", sans-serif; font-style: italic; font-weight: 700;
    font-size: 21px; color: var(--slate);
  }
  .panel {
    position: absolute; left: 516px; top: 0; width: 514px; height: 491px;
    background: linear-gradient(160deg, var(--panel-top) 0%, #2f7c15 55%, var(--panel-bottom) 100%);
    border-radius: 0 0 30px 30px;
  }
  .service {
    position: absolute; display: flex; align-items: center; gap: 14px;
    color: var(--white); font-weight: 700; font-size: 16.5px; line-height: 1.2;
    text-transform: uppercase; letter-spacing: 0.3px;
  }
  .service svg { width: 38px; height: 38px; flex: none; }
  .contact {
    position: absolute; left: 0; width: 100%; display: flex; justify-content: center; align-items: center; gap: 10px;
    color: var(--yellow); font-weight: 700; text-transform: uppercase; letter-spacing: 0.3px;
  }
  .contact.address { top: 276px; font-size: 15px; }
  .contact.email { top: 306px; font-size: 14px; }
  .call-band {
    position: absolute; left: 504px; top: 345px; width: 526px; height: 66px;
    background: linear-gradient(180deg, var(--yellow) 0%, var(--yellow-deep) 100%);
    display: flex; align-items: center; color: var(--ink-green); font-weight: 800;
  }
  .call-label { margin-left: 41px; font-size: 29px; letter-spacing: 1px; }
  .call-band svg { width: 44px; height: 44px; margin: 0 14px 0 10px; }
  .call-prefix { font-size: 32px; margin-right: 16px; }
  .call-number { font-size: 48px; letter-spacing: 1px; }
  .website {
    position: absolute; left: 516px; width: 514px; top: 428px; text-align: center;
    color: var(--yellow); font-weight: 800; font-size: 19px; letter-spacing: 0.6px;
  }
</style>
</head>
<body>
<main class="banner">
  <div class="photo" role="img" aria-label="Foto: graues Einfamilienhaus mit gepflegtem Vorgarten, Rasen, Bäumen und blauem Himmel"></div>

  <div class="brand">
    <p class="brand-name">Grünwerk Kessler GmbH</p>
    <div class="brand-rule"></div>
    <p class="brand-tagline">Garten- und Landschaftsbau Kessler</p>
  </div>

  <section class="panel">
    <div class="service" style="left:50px;top:52px">
      <svg viewBox="0 0 40 40"><circle cx="20" cy="20" r="18" fill="none" stroke="#fff" stroke-width="2"/><circle cx="20" cy="20" r="8" fill="#fff"/></svg>
      <span>Garten und<br>Landschafsbau</span>
    </div>
    <div class="service" style="left:50px;top:103px">
      <svg viewBox="0 0 40 40"><circle cx="20" cy="20" r="18" fill="none" stroke="#fff" stroke-width="2"/><path d="M11 16h16l-4 8h-9z" fill="#fff"/><circle cx="24" cy="27" r="3" fill="#fff"/></svg>
      <span>Baggerbetrieb</span>
    </div>
    <div class="service" style="left:50px;top:144px">
      <svg viewBox="0 0 40 40"><circle cx="20" cy="20" r="18" fill="none" stroke="#fff" stroke-width="2"/><rect x="13" y="14" width="14" height="8" fill="#fff"/><rect x="11" y="24" width="18" height="4" rx="2" fill="#fff"/></svg>
      <span>Erdbau</span>
    </div>
    <div class="service" style="left:50px;top:195px">
      <svg viewBox="0 0 40 40"><circle cx="20" cy="20" r="18" fill="none" stroke="#fff" stroke-width="2"/><rect x="13" y="11" width="10" height="18" fill="#fff"/><rect x="24" y="19" width="5" height="10" fill="#fff"/></svg>
      <span>Gebaude-<br>management</span>
    </div>
    <div class="service" style="left:277px;top:52px">
      <svg viewBox="0 0 40 40"><circle cx="20" cy="20" r="18" fill="none" stroke="#fff" stroke-width="2"/><circle cx="20" cy="17" r="7" fill="#fff"/><rect x="19" y="22" width="2" height="7" fill="#fff"/></svg>
      <span>Forst- und<br>Rodungsarbeiten</span>
    </div>
    <div class="service" style="left:277px;top:112px">
      <svg viewBox="0 0 40 40"><circle cx="20" cy="20" r="18" fill="none" stroke="#fff" stroke-width="2"/><path d="M20 28V16M20 18c-5 0-7-3-7-5 4 0 7 2 7 5zM20 16c0-4 3-6 7-6 0 3-3 6-7 6z" fill="#fff" stroke="#fff" stroke-width="1.5"/></svg>
      <span>Individuelle<br>Gartengestaltung</span>
    </div>
    <div class="service" style="left:277px;top:164px">
      <svg viewBox="0 0 40 40"><circle cx="20" cy="20" r="18" fill="none" stroke="#fff" stroke-width="2"/><path d="M13 12v16M18 12v16M23 12v16M28 12v16M11 17h19M11 23h19" stroke="#fff" stroke-width="2.5"/></svg>
      <span>Terassenbau</span>
    </div>
    <div class="service" style="left:277px;top:205px">
      <svg viewBox="0 0 40 40"><circle cx="20" cy="20" r="18" fill="none" stroke="#fff" stroke-width="2"/><path d="M12 22l8-8 4 4-8 8zM20 28l8-8-2-2-8 8z" fill="#fff"/></svg>
      <span>Plasterarbaiten</span>
    </div>

    <div class="contact address">
      <svg width="18" height="24" viewBox="0 0 18 24"><path d="M9 1a8 8 0 0 0-8 8c0 6 8 14 8 14s8-8 8-14a8 8 0 0 0-8-8z" fill="var(--yellow)"/><circle cx="9" cy="9" r="3" fill="#2f7c15"/></svg>
      <span>Lindenweg 4 55612 Talheim</span>
    </div>
    <div class="contact email">
      <svg width="22" height="16" viewBox="0 0 22 16"><rect width="22" height="16" fill="var(--yellow)"/><path d="M0 0l11 9L22 0" fill="none" stroke="#2f7c15" stroke-width="2"/></svg>
      <span>info@gruenwerk-kessler.de</span>
    </div>
  </section>

  <div class="call-band">
    <span class="call-label">JETZT</span>
    <svg viewBox="0 0 44 44"><circle cx="22" cy="22" r="20" fill="none" stroke="var(--ink-green)" stroke-width="2.5"/><path d="M17 12c-3 2-4 5-2 10s6 10 10 11c2 0 4-1 5-3l-4-4-3 2c-2-1-5-5-6-8l3-2-3-6z" fill="var(--ink-green)"/></svg>
    <span class="call-prefix">0151/</span>
    <span class="call-number">284907</span>
  </div>

  <div class="website">WWW.GRUENWERK-KESSLER.DE</div>
</main>
</body>
</html>
```